TAVRO Capital Group LLC a High Risk Big Rewards company for Rich Young Entrepreneurs

We would like a very modern, powerful in the eyes of our customers, modern, minimalist feel, financial gain. this business card is for young Rich entrepreneurs who want to invest money into High Risk, Big Rewards Businesses. The card Should sell the business!! let your creativity go Wild! I pick most of the designers for this project because of your BOLD Designs, I would like this card to be Bold, Modern, Minimalist, use as many effects in your graphic Artist Mind, Do not let the Financial sound of this business to make you think Conservative that's the last thing we are! if you have a lot of money and you want to play a risky market call US
Updates

Project Deadline Extended
Reason: have not received, enough designs to choose 1st and second place, sure I have received over 100 designs but it seems most designers are submitting every card they have ever made before and calling it mine, please we are looking for fresh ideas please!

Target Market(s)

Private Risky Investors

Industry/Entity Type

Financial

Contact Information for Business Card

powerful in the eyes of our customers,modern, minimalist feel

Font styles to use
Other font styles liked:
• Modern feeling fonts

Requirements
Must have
• The Company Name is TAVRO Capital Group LLC and it must be on the CARD
• My Name, title, Cell , email
• Delvin Ashcroft G.E.D.
• Managing Member
• 555.038.6195
• delvin@tavrocapitalgroup.example
Nice to have
• try a black thick plastic card with round corners with Delvin Ashcroft GED (make sure GED is smaller than name) just on one side of the card, and my phone number with out the icons and email on the other side, this card should look like a exclusive credit card or exclusive VIP card, something you would never loose

```html
<!DOCTYPE html>
<html lang="en">
<head>
<meta charset="utf-8">
<title>TAVRO Capital Group LLC — Business Card</title>
<link rel="stylesheet" href="https://fonts.googleapis.com/css2?family=Montserrat:wght@400;500;700&family=Open+Sans:ital,wght@1,400&display=swap">
<style>
  :root {
    --bg: #3a3d3d;
    --ink: #111111;
    --paper: #f4f4f4;
    --panel: #b9b9b9;
    --panel-band: #d6d6d6;
    --rule: #555555;
    --name-light: #d9d9d9;
    --text: #1e1e1e;
  }
  * { margin: 0; padding: 0; box-sizing: border-box; }
  html, body { width: 1200px; height: 900px; overflow: hidden; }
  body {
    background: var(--bg);
    display: flex;
    flex-direction: column;
    align-items: center;
    justify-content: center;
    gap: 40px;
    font-family: "Montserrat", sans-serif;
  }
  .card {
    position: relative;
    width: 700px;
    height: 400px;
    overflow: hidden;
  }

  /* Front */
  .card-front { background: var(--paper); }
  .front-band {
    position: absolute;
    top: 0; bottom: 0;
    left: 22%;
    width: 55%;
    background: var(--ink);
  }
  .front-name {
    position: absolute;
    left: calc(22% + 34px);
    top: 50%;
    transform: translateY(-20%);
    color: var(--name-light);
    font-weight: 700;
    font-size: 30px;
    line-height: 1.2;
    letter-spacing: 0.5px;
    text-transform: uppercase;
  }

  /* Back */
  .card-back { background: var(--ink); }
  .back-panel {
    position: absolute;
    inset: 16px;
    background: var(--panel);
    border: 3px solid #e4e4e4;
  }
  .back-band {
    position: absolute;
    top: 0; bottom: 0;
    left: 32%;
    width: 33%;
    background: var(--panel-band);
  }
  .back-company {
    position: absolute;
    left: 32%;
    width: 33%;
    top: 52px;
    text-align: center;
    color: var(--ink);
    font-weight: 700;
    font-size: 20px;
    line-height: 1.25;
    text-transform: uppercase;
  }
  .rule-top, .rule-bottom {
    position: absolute;
    left: 44px; right: 44px;
    height: 1px;
    background: var(--rule);
  }
  .rule-top { top: 138px; }
  .rule-bottom { top: 304px; }
  .rule-divider {
    position: absolute;
    left: 50%;
    top: 172px;
    height: 104px;
    width: 1px;
    background: var(--rule);
  }
  .holder {
    position: absolute;
    right: calc(50% + 22px);
    top: 204px;
    text-align: right;
    color: var(--text);
  }
  .holder-name { font-size: 17px; font-weight: 500; }
  .holder-name .credential { font-size: 14px; }
  .holder-title {
    font-family: "Open Sans", sans-serif;
    font-style: italic;
    font-size: 14px;
    margin-top: 2px;
  }
  .contact {
    position: absolute;
    left: calc(50% + 22px);
    top: 182px;
    color: var(--text);
    font-size: 15px;
    font-weight: 500;
    line-height: 1;
  }
  .contact li { list-style: none; }
  .contact li + li { margin-top: 22px; }
</style>
</head>
<body>

  <section class="card card-front" aria-label="Card front">
    <div class="front-band"></div>
    <h1 class="front-name">TAVRO Capital<br>Group LLC</h1>
  </section>

  <section class="card card-back" aria-label="Card back">
    <div class="back-panel">
      <div class="back-band"></div>
      <h2 class="back-company">TAVRO Capital<br>Group LLC</h2>
      <div class="rule-top"></div>
      <div class="rule-divider"></div>
      <div class="holder">
        <p class="holder-name">Delvin Ashcroft <span class="credential">G.E.D.</span></p>
        <p class="holder-title">Managing Member</p>
      </div>
      <ul class="contact">
        <li>555.038.6195</li>
        <li>delvin@tavrocapitalgroup.example</li>
      </ul>
      <div class="rule-bottom"></div>
    </div>
  </section>

</body>
</html>
```